'Recalibrating Columbia' is a political thriller novel

I need a book cover for a political thriller. The book is about a presidential campaign in 2024. A politician has a revolutionary new idea on how to move the economy from growing on debt based to thriving in abundance. A billionaire oil (Brandt) family undermines his campaign with blistering negative adds. A technology billionaire attempts to assassinate him. But ultimately the incumbent president seeking a third term will not give up power...
There is an underlying theory of economics told that is meant to educate the reader about how the majority of Americans and people around the world are trying to get by in a rigged system. Although the majority of people are much worse of then they need to be the truth is nobody is winning with the current economy (unless there sinister motivations involved). The story makes dire predictions of a technological dystopia.
Updates
Author's name: Tomas Ridley
Reason: There are so many very good choices but I haven't found the perfect one yer.
Target Market(s)
Anyone who is interested in living in a better world and changing what is not working and clearly getting worse.
Industry/Entity Type
Political
Colors
Designer to choose colors to be used in the design.
Look and feel
Each slider illustrates characteristics of the customer's brand and the style your logo design should communicate.

```html
<!DOCTYPE html>
<html lang="en">
<head>
<meta charset="utf-8">
<title>Recalibrating Columbia — Tomas Ridley</title>
<link href="https://fonts.googleapis.com/css2?family=Anton&family=Oswald:wght@700&display=swap" rel="stylesheet">
<style>
  :root {
    --paper: #f6f6f5;
    --paper-edge: #ebeae9;
    --title-red: #983a3c;
    --author-navy: #1f3258;
    --flag-navy: #3a4472;
    --flag-red: #a8444d;
    --flag-pale: #e9e2e3;
    --pole: #2a2a2c;
  }
  html, body {
    margin: 0;
    padding: 0;
    width: 768px;
    height: 1200px;
    overflow: hidden;
  }
  .cover {
    position: relative;
    width: 768px;
    height: 1200px;
    background: radial-gradient(ellipse at 50% 45%, var(--paper) 60%, var(--paper-edge) 100%);
    overflow: hidden;
  }
  .cover-title {
    position: absolute;
    top: 70px;
    left: 0;
    width: 768px;
    margin: 0;
    text-align: center;
    font-family: "Anton", "Oswald", sans-serif;
    font-weight: 400;
    color: var(--title-red);
    font-size: 118px;
    line-height: 138px;
    letter-spacing: 1px;
    text-transform: uppercase;
    transform: scaleY(1.2);
    transform-origin: top center;
  }
  .cover-title span { display: block; }
  .flag-pole {
    position: absolute;
    top: 388px;
    left: 32px;
    width: 10px;
    height: 812px;
    background: var(--pole);
    border-radius: 5px 5px 0 0;
  }
  .flag-photo {
    position: absolute;
    top: 428px;
    left: 44px;
    width: 708px;
    height: 405px;
    border-radius: 6px 40px 60px 10px;
    background:
      radial-gradient(ellipse at 22% 25%, var(--flag-navy) 0%, rgba(58,68,114,0.85) 30%, rgba(58,68,114,0) 55%),
      linear-gradient(170deg, var(--flag-red) 0%, #c07a80 45%, var(--flag-pale) 70%, var(--flag-red) 100%);
  }
  .author {
    position: absolute;
    top: 1100px;
    left: 0;
    width: 768px;
    margin: 0;
    text-align: center;
    font-family: "Oswald", sans-serif;
    font-weight: 700;
    font-size: 25px;
    line-height: 36px;
    letter-spacing: 4px;
    color: var(--author-navy);
    text-transform: uppercase;
  }
</style>
</head>
<body>
  <main class="cover">
    <h1 class="cover-title"><span>Recalibrating</span><span>Columbia</span></h1>
    <div class="flag-pole"></div>
    <div class="flag-photo" role="img" aria-label="Photograph of an American flag waving in the wind on a flagpole against a pale sky"></div>
    <p class="author">By Tomas Ridley</p>
  </main>
</body>
</html>
```